Need new Spot UV Business Card design

We are looking for a new business card design incorporating Spot UV in black & white options / versions. See examples files and Tobin Ashgrove Design logo.
You can see our website at www.tobinashgrove.ca. We want something classy but yet modern. We are open to black or black and/or white on white with the spot uv. We are open to portrait or landscape. Size should be standard 3.5" x 2". The front of the card should focus on the logo and name "Tobin Ashgrove" only. Fonts used should be "Open sans" or "PT Sans".

Target Market(s)

Mid to high end

Industry/Entity Type

Business

Contact Information for Business Card

Tobin Velasko
416.382.4417
tobin@tobinashgrove.ca
www.tobinashgrove.ca
4175 Brightwell Blvd. E Suite 308
Mississauga, ON L5T 2K9

Requirements
Must have
• Name & Logo

```html
<!DOCTYPE html>
<html lang="en">
<head>
<meta charset="utf-8">
<title>Tobin Ashgrove Design — Business Card</title>
<link rel="stylesheet" href="https://fonts.googleapis.com/css2?family=Montserrat:wght@300;400;600;700&display=swap">
<style>
  :root {
    --ink: #0b0b0b;
    --paper: #ffffff;
    --backdrop: #e4e2e0;
    --muted: #1a1a1a;
  }
  * { box-sizing: border-box; margin: 0; padding: 0; }
  html, body {
    width: 1200px;
    height: 800px;
    overflow: hidden;
    background: var(--backdrop);
    font-family: "Montserrat", sans-serif;
  }
  .canvas {
    position: relative;
    width: 1200px;
    height: 800px;
  }
  .card {
    position: absolute;
    top: 252px;
    width: 520px;
    height: 297px;
    box-shadow: 0 10px 30px rgba(0,0,0,0.18);
  }

  /* Back side: contact details */
  .card--back {
    left: 60px;
    background: var(--paper);
    color: var(--ink);
  }
  .card__bar {
    position: absolute;
    left: 250px;
    top: 0;
    width: 15px;
    height: 118px;
    background: var(--ink);
  }
  .card__rule {
    position: absolute;
    left: 256px;
    top: 118px;
    width: 3px;
    height: 179px;
    background: var(--ink);
  }
  .holder-name {
    position: absolute;
    right: 284px;
    top: 88px;
    font-weight: 700;
    font-size: 19px;
    letter-spacing: 0.2px;
    white-space: nowrap;
  }
  .contact-list {
    position: absolute;
    left: 243px;
    top: 122px;
    list-style: none;
  }
  .contact-list__item {
    display: flex;
    align-items: center;
    height: 40px;
  }
  .contact-list__icon {
    width: 30px;
    height: 30px;
    border-radius: 50%;
    background: var(--ink);
    display: flex;
    align-items: center;
    justify-content: center;
    flex-shrink: 0;
  }
  .contact-list__icon svg { width: 16px; height: 16px; }
  .contact-list__text {
    margin-left: 14px;
    font-size: 12.5px;
    font-weight: 600;
    line-height: 1.25;
    white-space: nowrap;
  }
  .brand--small {
    position: absolute;
    left: 30px;
    top: 180px;
    display: flex;
    align-items: center;
    gap: 7px;
  }
  .brand--small .brand__square {
    width: 14px;
    height: 14px;
    border: 1.5px solid var(--ink);
  }
  .brand--small .brand__name {
    font-weight: 400;
    font-size: 17px;
    letter-spacing: 0.5px;
    color: var(--ink);
  }

  /* Front side: name only */
  .card--front {
    left: 620px;
    background: var(--ink);
    color: var(--paper);
  }
  .brand--large {
    position: absolute;
    inset: 0;
    display: flex;
    flex-direction: column;
    align-items: center;
    justify-content: center;
    gap: 20px;
  }
  .brand--large .brand__square {
    width: 74px;
    height: 74px;
    border: 3px solid var(--paper);
  }
  .brand--large .brand__name {
    font-weight: 400;
    font-size: 34px;
    letter-spacing: 1px;
    color: var(--paper);
  }
</style>
</head>
<body>
<main class="canvas">

  <section class="card card--back" aria-label="Business card back">
    <div class="card__bar"></div>
    <div class="card__rule"></div>
    <p class="holder-name">Tobin Velasko</p>

    <ul class="contact-list">
      <li class="contact-list__item">
        <span class="contact-list__icon">
          <svg viewBox="0 0 24 24" aria-hidden="true"><path fill="#fff" d="M6.6 10.8c1.4 2.8 3.8 5.1 6.6 6.6l2.2-2.2c.3-.3.7-.4 1-.2 1.1.4 2.3.6 3.6.6.6 0 1 .4 1 1V20c0 .6-.4 1-1 1C10.6 21 3 13.4 3 4c0-.6.4-1 1-1h3.5c.6 0 1 .4 1 1 0 1.3.2 2.5.6 3.6.1.3 0 .7-.2 1l-2.3 2.2z"/></svg>
        </span>
        <span class="contact-list__text">416.382.4417</span>
      </li>
      <li class="contact-list__item">
        <span class="contact-list__icon">
          <svg viewBox="0 0 24 24" aria-hidden="true"><rect x="3" y="6" width="18" height="12" fill="none" stroke="#fff" stroke-width="2"/><path d="M3 6l9 7 9-7" fill="none" stroke="#fff" stroke-width="2"/></svg>
        </span>
        <span class="contact-list__text">tobin@tobinashgrove.ca</span>
      </li>
      <li class="contact-list__item">
        <span class="contact-list__icon">
          <svg viewBox="0 0 24 24" aria-hidden="true"><circle cx="12" cy="12" r="9" fill="none" stroke="#fff" stroke-width="2"/><ellipse cx="12" cy="12" rx="4" ry="9" fill="none" stroke="#fff" stroke-width="1.6"/><path d="M3 12h18" stroke="#fff" stroke-width="1.6"/></svg>
        </span>
        <span class="contact-list__text">www.tobinashgrove.ca</span>
      </li>
      <li class="contact-list__item">
        <span class="contact-list__icon">
          <svg viewBox="0 0 24 24" aria-hidden="true"><path d="M3 11l9-7 9 7M6 9v11h12V9" fill="none" stroke="#fff" stroke-width="2" stroke-linejoin="round"/><rect x="10" y="14" width="4" height="6" fill="#fff"/></svg>
        </span>
        <span class="contact-list__text">4175 Brightwell Blvd. E Suite 308<br>Mississauga, ON L5T 2K9</span>
      </li>
    </ul>

    <div class="brand brand--small">
      <span class="brand__square"></span>
      <span class="brand__name">TOBIN ASHGROVE</span>
    </div>
  </section>

  <section class="card card--front" aria-label="Business card front">
    <div class="brand brand--large">
      <span class="brand__square"></span>
      <span class="brand__name">TOBIN ASHGROVE</span>
    </div>
  </section>

</main>
</body>
</html>
```